Lotvantage.com Webpage Design

Design Brief for lotvantage.com (Copy of Brief also in attached Word file)

Name of Website- lotvantage.com (existing logo and look & feel of website to be changed)

Logo - Finalised. The logo files are attached with the brief as “logo.jpeg”. The “Blue- Grey” version of the logo is for use on lighter backgrounds and the “Orange-White” version of the logo is for use on darker backgrounds. (A full Black version of the logo is also attached). Both versions may be used in different parts of the website. All attached files are in .png format.
Status - The website in functional and is undergoing user trials. However, we want to improve the look & feel of the website so at it seems
a. cotemporary,
b. Easy to Navigate
c. professional and
d. Vibrant.

Please visit ‘lotvantage.com’ to check out the website and its functionalities – please use it only as a reference for the features & functions to be provided, however the designer should use a ‘Free Hand’ in designing the composition of various parts of the webpage without getting too influenced by the existing design

Objective of the Website ‘lotvantage.com –
a. It is a portal focussed on listing of ‘Retail’ specific real-estate properties by developers, owners and realty brokers. The properties shall listed under the following four categories-
i. Retail Malls
ii. Shopping Complexes
iii. High-street shops
iv. Retail Warehouses
*refer lotvantage.com for better clarity

b. The abovementioned properties shall be listed either for ‘Sale’ or ‘rent\lease’ or both

c. Users shall visit the site in case they wish to acquire a retail \ shop space either on ‘sale’ or ‘rent’. These Users would be able to specify the ‘Search Criteria’ through the tool-bars provided on the website – the ‘Search Criteria’ shall comprise of ‘Type of space category’, ‘City’, ‘Locality’, transaction type ie ‘Rent \ Sale’ and ‘Area Range’

d. The main revenue model for the website shall be listing fee ( or advertising charges ) payable by those listing their properties on the website.

Three Main Pages of Website (lotvantage.com) that need to be designed -
a. Main Home Page (visit the web link - http://lotvantage.com/ ) - The main home page has the “Search Toolbar” for specifying of Search Criteria by the User. It shall also have the following features & functions-
i. Main Advertising Banner
ii. Featured Projects
iii. New Launches
iv. Toolbar with buttons – ‘Advertise with Us’, ‘Listings Alert’, ‘Lot Mavens’, ‘Advertiser Login’

b. Property Listings Page (visit the web link - http://lotvantage.com/gurgaon-in-india ) - The List of property options that match the Criteria specified by the ‘User’ get displayed on this page.

c. Property Detail Page - When the ‘User’ clicks on the “More….” Button on the ‘Property Listings Page’ (given in point b. above) the web page with the details of the property opens. (For Example – visit the web link - http://lotvantage.com/brevo-Shopping-Complex-brevo-quadrel-gurgaon-636 )

Note:- Please refer to attached ‘Shopping’ related images the designer may use them on the website to provide a look & feel of retail if required – either separately or rotate in a single window

Target Market(s)

Retailers & Investors looking for retail space, Real Estate Brokers, Developers

Industry/Entity Type

Advertising

Number of Pages Required

3 page

Requirements
Must have
• Refer to existing site lotvantage.com -- all the existing functionalities are a must have.
Nice to have
• The Designer may use the retail related images on the website if required for making it more vibrant. Refer attached images Shopping(1-6).jpg

```html
<!DOCTYPE html>
<html lang="en">
<head>
<meta charset="utf-8">
<title>Lotvantage.com – Home</title>
<link href="https://fonts.googleapis.com/css2?family=Open+Sans:wght@400;600;700&display=swap" rel="stylesheet">
<style>
:root{
  --blue:#4a90e2;
  --blue-dark:#2f6fbf;
  --ink:#222;
  --muted:#555;
  --page:#ececee;
  --panel:#fff;
  --line:#cfd0d3;
  --footer:#f5f5f6;
  --bottom:#e4e5e7;
  --orange:#e0692a;
  --grey-star:#c7c7c7;
  --dark:#1b1f26;
}
*{box-sizing:border-box;margin:0;padding:0}
html,body{width:1200px;height:1000px;overflow:hidden;background:#fff;font-family:"Open Sans",Arial,sans-serif;color:var(--ink)}
.site{position:absolute;left:172px;top:0;width:860px;height:1000px;background:var(--page)}
.abs{position:absolute}

/* city bar */
.city-bar{left:0;top:0;width:860px;height:16px;background:#f4f4f5;border-top:2px solid var(--blue);display:flex;justify-content:center;gap:0;font-size:8px;color:var(--blue-dark);line-height:13px}
.city-bar span{padding:0 9px;border-right:1px solid #bbb}
.city-bar span:last-child{border-right:0}

/* header */
.header{left:0;top:16px;width:860px;height:44px;background:var(--panel)}
.brand{left:124px;top:10px;display:flex;align-items:center;gap:6px;font-size:19px;font-weight:700;color:var(--blue-dark)}
.brand i{display:block;width:18px;height:18px;border-radius:50%;background:var(--blue)}
.nav{left:302px;top:16px;display:flex;gap:30px;font-size:8.5px;color:#333}
.nav .active{color:var(--blue)}
.login{left:597px;top:8px;width:110px;height:22px;background:var(--blue);border:1px solid var(--blue-dark);color:#fff;font-size:9px;font-weight:700;text-align:center;line-height:20px}

/* hero */
.hero{left:0;top:60px;width:860px;height:153px;background:linear-gradient(100deg,#6a6f78 0%,#9a6a55 35%,#8a8f98 60%,#5d6670 100%)}
.hero-title{left:114px;top:86px;font-size:20px;font-weight:700;color:var(--blue)}
.hero-sub{left:114px;top:113px;font-size:12.5px;font-weight:700;color:#fff}
.hero-card{left:594px;top:145px;width:168px;height:38px;background:var(--dark);color:#fff;font-size:7px}
.hero-card .info{position:absolute;left:0;top:0;width:110px;text-align:center;line-height:10px;padding-top:2px}
.hero-card .info b{font-size:7.5px}
.hero-card .info .area{display:block;border-top:1px solid #444;margin-top:3px;padding-top:2px}
.hero-card .price{position:absolute;left:110px;top:0;width:58px;height:38px;border-left:1px solid #444;text-align:center;padding-top:4px}
.hero-card .price b{display:block;font-size:12px}

/* search */
.tabs{left:114px;top:187px;width:648px;height:25px;display:flex}
.tabs div{flex:1;background:#dcdde0;border:1px solid var(--line);font-size:8px;color:#999;text-align:center;line-height:23px}
.tabs .on{background:#fff;border-bottom:0;color:#666}
.search{left:114px;top:212px;width:648px;height:63px;background:#fff;border:1px solid var(--line);border-top:0}
.field{position:absolute;top:18px;height:22px;border:1px solid #bbb;border-radius:2px;font-size:7.5px;line-height:20px;padding-left:7px;color:#333;background:#fff}
.field:after{content:"";position:absolute;right:6px;top:7px;border:3px solid transparent;border-top-color:#333}
.field.text{color:#999;border-color:#ccc}
.field.text:after{display:none}
.btn-search{position:absolute;left:502px;top:17px;width:117px;height:23px;background:var(--blue);border:1px solid var(--blue-dark);color:#fff;font-size:8.5px;font-weight:700;text-align:center;line-height:21px}

/* listings */
.section-title{font-size:9.5px;font-weight:700;color:var(--blue)}
.arrows{display:flex;gap:3px}
.arrows i{display:block;width:9px;height:8px;background:#777}
.card{position:absolute;width:150px;height:176px;background:#fff;border:1px solid #c4c5c8;box-shadow:0 1px 2px rgba(0,0,0,.15)}
.card .photo{position:absolute;left:6px;top:8px;width:136px;height:72px}
.card .tag{position:absolute;right:6px;top:8px;background:#2b2b2b;color:#fff;font-size:7px;padding:2px 5px}
.card .body{position:absolute;left:6px;top:88px;width:136px;height:84px;border-left:1px solid var(--blue);padding-left:6px}
.card .city{font-size:9.5px;font-weight:700;color:var(--blue);margin-top:2px}
.card .name{font-size:7.5px;font-weight:700;margin-top:9px;line-height:11px}
.card .loc{font-size:7.5px;color:var(--muted);line-height:11px}
.card .type{font-size:7.5px;font-weight:700;line-height:11px}
.card .view{position:absolute;left:6px;top:66px;border:1px solid #aaa;border-radius:2px;background:linear-gradient(#fff,#e9e9e9);font-size:7.5px;padding:2px 7px}
.meta{position:absolute;width:150px;height:14px;display:flex;justify-content:space-between;align-items:baseline}
.stars{font-size:10px;letter-spacing:0}
.stars .b{color:var(--blue)}.stars .o{color:var(--orange)}.stars .g{color:var(--grey-star)}
.rate{font-size:10px;font-weight:700}
.rate small{font-size:6px;font-weight:400;vertical-align:top}

/* footer */
.footer{left:0;top:769px;width:860px;height:186px;background:var(--footer);border-top:1px solid #d8d8da}
.fcol-title{font-size:10px;font-weight:700;color:var(--blue)}
.links{font-size:7.5px;line-height:10.9px;padding-left:17px}
.news{width:200px}
.news .date{position:absolute;left:0;top:0;width:32px;height:34px;border:1px solid #bbb;background:#fff;text-align:center}
.news .date b{display:block;font-size:11px;line-height:19px;border-bottom:1px solid #ccc}
.news .date span{font-size:6.5px;color:#777}
.news h4{margin-left:39px;font-size:8.5px;font-weight:700}
.news .by{margin-left:39px;font-size:6.5px;color:#888}
.news p{margin-left:39px;font-size:7.5px;color:var(--muted);line-height:11.5px;margin-top:3px}
.address{font-size:7.5px;line-height:11.6px;color:#333}
.bottom{left:0;top:955px;width:860px;height:45px;background:var(--bottom)}
.copy{left:331px;top:15px;font-size:7.5px;color:#444}
.social{left:646px;top:11px;display:flex;gap:6px}
.social i{display:block;width:18px;height:18px;border:1.5px solid #222;border-radius:50%}
</style>
</head>
<body>
<div class="site">

  <div class="abs city-bar">
    <span>Bangalore</span><span>Chennai</span><span>Greater Noida</span><span>Gurgaon</span><span>Hyderabad</span><span>Jaipur</span><span>Khanna</span><span>Kolkatta</span><span>Mumbai</span><span>Noida</span><span>Pune</span><span>Surat</span>
  </div>

  <header class="abs header">
    <div class="abs brand"><i></i>lotvantage.com</div>
    <nav class="abs nav"><span class="active">Home</span><span>Advertise with us</span><span>Lot Mavens</span><span>Listing Alert</span></nav>
    <div class="abs login">&#128100; LOGIN / REGISTER</div>
  </header>

  <div class="abs hero" role="img" aria-label="Banner photograph of a glass and brick shopping mall facade with trees"></div>
  <div class="abs hero-title">Harbor Arcade</div>
  <div class="abs hero-sub">Royapettah , Chennai</div>
  <div class="abs hero-card">
    <div class="info"><b>HARBOR ARCADE</b><br>Royapettah, Chennai<span class="area">over 900,000 square feet.</span></div>
    <div class="price"><b>$2000</b>per month</div>
  </div>

  <div class="abs tabs">
    <div class="on">RETAIL MALLS</div><div>SHOPPING COMPLEX</div><div>HIGH STREETS SHOPS</div><div>RETAIL WAREHOUSES</div>
  </div>
  <div class="abs search">
    <div class="field" style="left:22px;width:82px">Sale</div>
    <div class="field" style="left:115px;width:84px">Select City</div>
    <div class="field" style="left:208px;width:134px">Select Locality/Micro-Market</div>
    <div class="field text" style="left:352px;width:140px">Name of Project, Developer, etc</div>
    <div class="btn-search">&#128269; SEARCH</div>
  </div>

  <div class="abs section-title" style="left:114px;top:284px">FEATURED PROJECTS</div>
  <div class="abs arrows" style="left:742px;top:292px"><i></i><i></i></div>

  <div class="card" style="left:114px;top:304px">
    <div class="photo" role="img" aria-label="Photo of a hotel and retail tower lit at dusk" style="background:linear-gradient(#2c3a5a,#6b6a70 70%,#3a3a40)"></div><div class="tag">Sale/Rent</div>
    <div class="body"><div class="city">FARIDABAD</div><div class="name">Verma 81 High Street</div><div class="loc">Sector-81</div><div class="type">Shopping Complex</div><div class="view">&#128065; View Listing</div></div>
  </div>
  <div class="card" style="left:280px;top:304px">
    <div class="photo" role="img" aria-label="Aerial view of a mixed-use commercial complex among trees" style="background:linear-gradient(#a9c3d9,#7d8f86 55%,#4f6e4a)"></div><div class="tag">Sale/Rent</div>
    <div class="body"><div class="city">GURGAON</div><div class="name">K2K Metropolitan</div><div class="loc">Sector-65</div><div class="type">Shopping Complex</div><div class="view">&#128065; View Listing</div></div>
  </div>
  <div class="card" style="left:446px;top:304px">
    <div class="photo" role="img" aria-label="Golden lit tower against a blue night sky" style="background:linear-gradient(#1d3a7a,#3b5ea0 60%,#9a7a3a)"></div><div class="tag">Sale/Rent</div>
    <div class="body"><div class="city">GURGAON</div><div class="name">Orvin 24K</div><div class="loc">Sohna Road</div><div class="type">Retail Malls</div><div class="view">&#128065; View Listing</div></div>
  </div>
  <div class="card" style="left:612px;top:304px">
    <div class="photo" role="img" aria-label="Shopping mall exterior with plaza and billboards" style="background:linear-gradient(#b8c2cc,#6e6f75 55%,#4d4d52)"></div><div class="tag">Sale/Rent</div>
    <div class="body"><div class="city">NEW DELHI</div><div class="name">Meridian Mall-Tagore Garden</div><div class="loc">Tagore Garden</div><div class="type">Retail Malls</div><div class="view">&#128065; View Listing</div></div>
  </div>

  <div class="meta" style="left:114px;top:483px"><span class="stars"><span class="b">★</span><span class="o">★★</span><span class="g">★★</span></span><span class="rate">$2,150<small> /mo</small></span></div>
  <div class="meta" style="left:280px;top:483px"><span class="stars"><span class="b">★</span><span class="o">★★</span><span class="g">★★</span></span><span class="rate">$2,150<small> /mo</small></span></div>
  <div class="meta" style="left:446px;top:483px"><span class="stars"><span class="b">★</span><span class="o">★★</span><span class="g">★★</span></span><span class="rate">$2,150<small> /mo</small></span></div>
  <div class="meta" style="left:612px;top:483px"><span class="stars"><span class="b">★</span><span class="o">★★</span><span class="g">★★</span></span><span class="rate">$2,150<small> /mo</small></span></div>

  <div class="abs section-title" style="left:114px;top:531px">FEATURED NEW LAUNCHES</div>
  <div class="abs arrows" style="left:742px;top:539px"><i></i><i></i></div>

  <div class="card" style="left:114px;top:551px">
    <div class="photo" role="img" aria-label="Rendering of a mall entrance with green terraces" style="background:linear-gradient(90deg,#c9c2b6,#9a4a55 50%,#d8d2c8)"></div><div class="tag">Sale/Rent</div>
    <div class="body"><div class="city">BHOPAL</div><div class="name">The Grand Bazaar Place</div><div class="loc">Kolar Road</div><div class="type">Retail Malls</div><div class="view">&#128065; View Listing</div></div>
  </div>
  <div class="card" style="left:280px;top:551px">
    <div class="photo" role="img" aria-label="Rendering of a glass tower over a lit retail podium" style="background:linear-gradient(#2a4f8a,#5a6f90 60%,#7a3a4a)"></div><div class="tag">Sale/Rent</div>
    <div class="body"><div class="city">NOIDA</div><div class="name">Crest One</div><div class="loc">Sector-18</div><div class="type">Retail Malls</div><div class="view">&#128065; View Listing</div></div>
  </div>
  <div class="card" style="left:446px;top:551px">
    <div class="photo" role="img" aria-label="Rendering of a low-rise retail strip with towers behind" style="background:linear-gradient(#b7c9df,#8a8f95 55%,#6e7a60)"></div><div class="tag">Sale/Rent</div>
    <div class="body"><div class="city">MOHALI</div><div class="name">Urban Core - SCO In Sector</div><div class="loc">Sihon Majra</div><div class="type">Shopping Complex</div><div class="view">&#128065; View Listing</div></div>
  </div>
  <div class="card" style="left:612px;top:551px">
    <div class="photo" role="img" aria-label="Rendering of a low-rise retail strip with towers behind" style="background:linear-gradient(#b7c9df,#8a8f95 55%,#6e7a60)"></div><div class="tag">Sale/Rent</div>
    <div class="body"><div class="city">MOHALI</div><div class="name">SCO In Sector 127 On</div><div class="loc">Sihon Majra</div><div class="type">Shopping Complex</div><div class="view">&#128065; View Listing</div></div>
  </div>

  <div class="meta" style="left:114px;top:729px"><span class="stars"><span class="b">★</span><span class="o">★★</span><span class="g">★★</span></span><span class="rate">$2,150<small> /mo</small></span></div>
  <div class="meta" style="left:280px;top:729px"><span class="stars"><span class="b">★</span><span class="o">★★</span><span class="g">★★</span></span><span class="rate">$2,150<small> /mo</small></span></div>
  <div class="meta" style="left:446px;top:729px"><span class="stars"><span class="b">★</span><span class="o">★★</span><span class="g">★★</span></span><span class="rate">$2,150<small> /mo</small></span></div>
  <div class="meta" style="left:612px;top:729px"><span class="stars"><span class="b">★</span><span class="o">★★</span><span class="g">★★</span></span><span class="rate">$2,150<small> /mo</small></span></div>

  <footer class="abs footer">
    <div class="abs fcol-title" style="left:114px;top:14px">ABOUT SHOPFRONT HUB</div>
    <ul class="abs links" style="left:114px;top:35px">
      <li>About Us</li><li>Privacy Policy</li><li>Terms of Use</li><li>Contact Us</li><li>Site Map</li><li>Retail Malls</li><li>Shopping Complex</li><li>High Street Shops</li><li>Retail Warehouses</li>
    </ul>

    <div class="abs fcol-title" style="left:335px;top:14px">RECENT NEWS</div>
    <div class="abs news" style="left:336px;top:33px">
      <div class="date"><b>20</b><span>mar</span></div>
      <h4>How to Choose Property</h4><div class="by">posted by admin</div>
      <p>In porttitor augue vel velit luctus at scelerisque nisi dictum. Ut tempus dignissim mi, at gravida leo.</p>
    </div>
    <div class="abs news" style="left:336px;top:103px">
      <div class="date"><b>16</b><span>mar</span></div>
      <h4>Real Estate of Future</h4><div class="by">posted by admin</div>
      <p>In porttitor augue vel velit luctus at scelerisque nisi dictum. Ut tempus dignissim mi, at gravida leo.</p>
    </div>

    <div class="abs fcol-title" style="left:557px;top:14px">CONTACT</div>
    <div class="abs address" style="left:574px;top:35px">
      Shopfront Hub<br>Unit 406, 4th Floor,<br>Lorem Ipsum is simply,<br>Sector-x, Gurgaon - 122002<br><br>Phone: 000-000-0000<br>Fax: 000-000-0000
    </div>
  </footer>

  <div class="abs bottom">
    <div class="abs brand" style="left:124px;top:12px"><i></i>lotvantage.com</div>
    <div class="abs copy">Copyright © 2015 India Shopfront Hub.com. All rights reserved.</div>
    <div class="abs social"><i></i><i></i><i></i><i></i><i></i></div>
  </div>

</div>
</body>
</html>
```